Dunmore Plumbing LLC business card

Would like a modern looking business card with my new logo

Contact Information for Business Card

Calvin Dunmore 2418 Elm Hollow Rd Southbury, CT 06999, Dunmoreplumbingllc@exampletrade.com, 203-555-0174

```html
<!DOCTYPE html>
<html lang="en">
<head>
<meta charset="utf-8">
<title>Dunmore Plumbing LLC – Business Card</title>
<link href="https://fonts.googleapis.com/css2?family=Open+Sans:wght@300;400;700&display=swap" rel="stylesheet">
<style>
  :root {
    --page-bg: #e9e7e3;
    --card-white: #ffffff;
    --ink: #111111;
    --muted: #555555;
    --accent: #2aa6e0;
    --rule: #222222;
    --navy-deep: #1a2230;
    --navy-light: #4a5567;
    --silver: #e6e8eb;
  }
  * { margin: 0; padding: 0; box-sizing: border-box; }
  html, body {
    width: 1200px; height: 1200px; overflow: hidden;
    background: var(--page-bg);
    font-family: "Open Sans", Arial, sans-serif;
  }
  .sheet {
    width: 1200px; height: 1200px;
    display: flex; flex-direction: column; align-items: center; justify-content: center;
    gap: 80px;
  }
  .card {
    position: relative;
    width: 700px; height: 400px;
    box-shadow: 0 10px 30px rgba(0,0,0,0.18);
    overflow: hidden;
  }
  /* Front */
  .card-front { background: var(--card-white); color: var(--ink); }
  .brand-name {
    position: absolute; top: 52px; right: 60px;
    font-weight: 700; font-size: 44px; letter-spacing: 1px;
    text-transform: uppercase; line-height: 1; text-align: right;
    color: var(--ink);
  }
  .brand-name .brand-sub {
    display: block; font-size: 20px; letter-spacing: 6px; margin-top: 8px;
  }
  .person-name {
    position: absolute; top: 172px; left: 56px;
    color: var(--accent); font-weight: 300; font-size: 30px; letter-spacing: 0.5px;
  }
  .person-role {
    position: absolute; top: 216px; left: 56px; right: 40px;
    display: flex; align-items: center; gap: 10px;
    color: var(--muted); font-size: 15px;
  }
  .person-role::after {
    content: ""; flex: 1; height: 1.5px; background: var(--rule);
  }
  .contact-list {
    position: absolute; top: 250px; left: 56px;
    list-style: none; color: var(--muted); font-size: 15px; line-height: 1.55;
  }
  .contact-list li { display: flex; align-items: center; gap: 10px; }
  .contact-list svg { width: 14px; height: 14px; fill: var(--accent); flex: none; }
  .address {
    position: absolute; right: 56px; bottom: 36px;
    display: flex; align-items: flex-end; gap: 12px;
    color: var(--muted); font-size: 15px; text-align: right; line-height: 1.45;
  }
  .address svg { width: 18px; height: 24px; fill: var(--accent); margin-bottom: 22px; }

  /* Back */
  .card-back {
    background: radial-gradient(ellipse at 60% 55%, var(--navy-light) 0%, #323c4d 45%, var(--navy-deep) 100%);
    display: flex; align-items: center; justify-content: center;
  }
  .card-back .texture {
    position: absolute; inset: 0;
    background: linear-gradient(135deg, rgba(255,255,255,0.04), rgba(0,0,0,0.12));
  }
  .back-brand {
    position: relative; text-align: center;
    color: var(--silver); font-weight: 700; text-transform: uppercase; line-height: 1;
    font-size: 62px; letter-spacing: 2px;
  }
  .back-brand .brand-sub {
    display: block; font-size: 24px; letter-spacing: 8px; margin-top: 12px;
  }
</style>
</head>
<body>
  <main class="sheet">
    <section class="card card-front" aria-label="Business card front">
      <div class="brand-name">Dunmore<span class="brand-sub">Plumbing LLC</span></div>
      <h1 class="person-name">CALVIN DUNMORE</h1>
      <p class="person-role">Founder</p>
      <ul class="contact-list">
        <li>
          <svg viewBox="0 0 24 24" aria-hidden="true"><path d="M6.6 10.8a15.1 15.1 0 0 0 6.6 6.6l2.2-2.2a1 1 0 0 1 1-.25 11.4 11.4 0 0 0 3.6.57 1 1 0 0 1 1 1V20a1 1 0 0 1-1 1A17 17 0 0 1 3 4a1 1 0 0 1 1-1h3.5a1 1 0 0 1 1 1c0 1.25.2 2.45.57 3.57a1 1 0 0 1-.25 1z"/></svg>
          203-555-0174
        </li>
        <li>
          <svg viewBox="0 0 24 24" aria-hidden="true"><path d="M12 2a10 10 0 1 0 0 20 10 10 0 0 0 0-20zm6.9 6h-3a15.7 15.7 0 0 0-1.4-3.6A8 8 0 0 1 18.9 8zM12 4a14 14 0 0 1 1.9 4h-3.8A14 14 0 0 1 12 4zM4.3 14a8 8 0 0 1 0-4h3.4a16.5 16.5 0 0 0 0 4zm.8 2h3a15.7 15.7 0 0 0 1.4 3.6A8 8 0 0 1 5.1 16zm3-8h-3a8 8 0 0 1 4.3-3.6A15.7 15.7 0 0 0 8.1 8zM12 20a14 14 0 0 1-1.9-4h3.8A14 14 0 0 1 12 20zm2.3-6H9.7a14.7 14.7 0 0 1 0-4h4.6a14.7 14.7 0 0 1 0 4zm.3 5.6a15.7 15.7 0 0 0 1.4-3.6h3a8 8 0 0 1-4.4 3.6zM16.3 14a16.5 16.5 0 0 0 0-4h3.4a8 8 0 0 1 0 4z"/></svg>
          www.dunmoreplumbingllc.example
        </li>
        <li>
          <svg viewBox="0 0 24 24" aria-hidden="true"><path d="M2 5h20v14H2zm2 2v.5l8 5 8-5V7zm0 2.9V17h16V9.9l-8 5z"/></svg>
          Dunmoreplumbingllc@exampletrade.com
        </li>
      </ul>
      <div class="address">
        <p>2418 Elm Hollow Rd<br>Southbury, CT 06999</p>
        <svg viewBox="0 0 18 24" aria-hidden="true"><path d="M9 0a9 9 0 0 0-9 9c0 6.5 9 15 9 15s9-8.5 9-15a9 9 0 0 0-9-9zm0 12.5A3.5 3.5 0 1 1 9 5.5a3.5 3.5 0 0 1 0 7z"/></svg>
      </div>
    </section>

    <section class="card card-back" aria-label="Business card back">
      <div class="texture" role="img" aria-label="Dark blue-grey textured metal backdrop"></div>
      <div class="back-brand">Dunmore<span class="brand-sub">Plumbing LLC</span></div>
    </section>
  </main>
</body>
</html>
```